Vell Partners Building Business Cards

We need a business card that reflects our business as "Solar Experts" in San Diego. Browse our website www.vellpartners.example our License needs to be displayed as "CSLB# 4718392" our phone number is (619) 555-0147

Save thousands on your electric bills and increase the value of your home while helping to protect the environment. Our solar installation experts will help you design the system that's right for you, using only the highest quality equipment that will look great and give you ideal performance. Our goal is to make you energy independent, and get your electric bill to 0.

Tobias Wrenfield
(619) 555-0147
tobias@vellpartners.example

Target Market(s)

Home owners in san diego looking for solar

Industry/Entity Type

Solar Energy

Contact Information for Business Card

Tobias Wrenfield
(619) 555-0147
tobias@vellpartners.example

Font styles to use
Other font styles liked:
• Use our logo font

Requirements
Must have
• License needs to be displayed as "CSLB# 4718392" our phone number is (619) 555-0147
Nice to have
• Real images of rooftop home solar in san diego
Should not have
• our business address

```html
<!DOCTYPE html>
<html lang="en">
<head>
<meta charset="utf-8">
<title>Vell Partners Building – Business Card</title>
<link rel="stylesheet" href="https://fonts.googleapis.com/css2?family=Libre+Franklin:wght@400;600;700&display=swap">
<style>
  :root {
    --navy: #173d78;
    --sun: #f7b000;
    --white: #ffffff;
    --backdrop: #262626;
  }
  * { margin: 0; padding: 0; box-sizing: border-box; }
  html, body {
    width: 1200px; height: 987px; overflow: hidden;
    background: var(--backdrop);
    font-family: "Libre Franklin", Arial, sans-serif;
  }
  .card {
    position: absolute; left: 293px; width: 615px; height: 350px;
    overflow: hidden;
  }
  .card--front { top: 131px; background: var(--navy); }
  .card--back { top: 506px; background: var(--sun); color: var(--white); }

  .front-swoosh { position: absolute; inset: 0; width: 100%; height: 100%; }

  .contact { position: absolute; left: 33px; top: 32px; color: var(--white); z-index: 1; }
  .contact__name { font-size: 21px; font-weight: 600; color: var(--sun); line-height: 1.2; }
  .contact__title { font-size: 16px; margin-top: 2px; }
  .contact__license { font-size: 15px; margin-top: 26px; }
  .contact__list { list-style: none; margin-top: 14px; font-size: 13.5px; }
  .contact__list li { display: flex; align-items: center; gap: 6px; height: 23.5px; white-space: nowrap; }
  .contact__list svg { width: 15px; height: 15px; flex: none; fill: var(--sun); }

  .wordmark {
    position: absolute; right: 40px; bottom: 60px;
    font-size: 27px; font-weight: 700; color: var(--navy);
    letter-spacing: -0.3px;
  }

  .back-brand {
    position: absolute; left: 0; right: 0; top: 110px;
    display: flex; flex-direction: column; align-items: center; gap: 18px;
  }
  .back-brand__dot { width: 70px; height: 70px; border-radius: 50%; background: var(--white); }
  .back-brand__name { font-size: 30px; font-weight: 700; }
  .back-url {
    position: absolute; left: 0; right: 0; top: 295px; text-align: center;
    font-size: 15px; letter-spacing: 3.5px;
  }
</style>
</head>
<body>
  <section class="card card--front">
    <svg class="front-swoosh" viewBox="0 0 615 350" preserveAspectRatio="none" aria-hidden="true">
      <path d="M150 350 Q268 80 570 14 Q315 100 180 350 Z" fill="var(--white)"/>
      <path d="M154 350 Q270 84 564 16 Q315 104 180 350 Z" fill="var(--sun)"/>
      <path d="M180 350 Q318 64 615 2 L615 350 Z" fill="var(--white)"/>
    </svg>
    <div class="contact">
      <p class="contact__name">Tobias Wrenfield</p>
      <p class="contact__title">CEO/Founder</p>
      <p class="contact__license">CSLB# 4718392</p>
      <ul class="contact__list">
        <li><svg viewBox="0 0 16 16"><path d="M2 5c0-2 3-3 6-3s6 1 6 3v1h-3V5H5v1H2z M4 7h8l2 6H2z"/></svg>(619) 555-0147</li>
        <li><svg viewBox="0 0 16 16"><path d="M1 3h14v2L8 9 1 5z M1 7l7 4 7-4v6H1z"/></svg>tobias@vellpartners.example</li>
        <li><svg viewBox="0 0 16 16"><circle cx="8" cy="8" r="7"/><path d="M5 4l3 2-1 3 3 1-1 3" stroke="var(--navy)" stroke-width="1.4" fill="none"/></svg>www.vellpartners.example</li>
      </ul>
    </div>
    <p class="wordmark">Vell Partners Building</p>
  </section>

  <section class="card card--back">
    <div class="back-brand">
      <span class="back-brand__dot"></span>
      <p class="back-brand__name">Vell Partners Building</p>
    </div>
    <p class="back-url">www.vellpartners.example</p>
  </section>
</body>
</html>
```